Landingpage design

We need a landingpage for a chatterloop add campaign. We sell socks made of bamboo in super quality. Our customers loves us, and we have a 5 heart rating at opinivo.com.

We want to create a add campaign targeted new customers, and the offer is that they can buy 1 pair of bamboo socks as a test, for only 20 DKK (2,7 Euro) including shipment. Our webpage is www.lintora.dk, landingpage should be built i Pagmoro, a wysiwyg editor. based on their template. like:
https://lintora.pagmoro.com/13844-sales-page
https://lintora.pagmoro.com/13696-sales-page
https://lintora.pagmoro.com/13845-sales-page

You don't have to follow the templates 100% if you have better ideas. We have an account for snapquarry, so please get stockphotos from here.

Bamboo socks has a lot of great selling points, you can see a good desciption here:
https://tovelin.com/us/why-bamboo

We expect you to have experience in landingpage design, and expect to end up with 2 landingpages we can splittest on.

This is the first of a number of landingpages we need in the future, so for the right person there will be plenty of more work.

Target Market(s)

Denmark

Industry/Entity Type

E-Commerce

Number of Pages Required

2 page

Colors

Designer to choose colors to be used in the design.

Requirements
Must have
• A great selling page, showing all the great things with bamboo socks. It should be supplied with good packshots from snapquarry.com

```html
<!DOCTYPE html>
<html lang="da">
<head>
<meta charset="utf-8">
<title>Lintora – Basics i bambus</title>
<link href="https://fonts.googleapis.com/css2?family=Jost:wght@300;400;500;600&family=Poppins:wght@300;400;600&display=swap" rel="stylesheet">
<style>
:root{
  --yellow:#f7b92f;
  --yellow-deep:#eea91c;
  --black:#050505;
  --ink:#2a2a2a;
  --grey-text:#555;
  --card-line:#e2e2e2;
  --welcome-bg:#f0f0f0;
  --footer-bg:#1c1a1b;
  --footer-line:#333;
  --footer-text:#e6e6e6;
  --white:#fff;
}
*{box-sizing:border-box;margin:0;padding:0}
html,body{width:1200px;height:2514px;overflow:hidden}
body{position:relative;background:var(--white);font-family:"Jost",sans-serif;color:var(--ink)}
.abs{position:absolute}

/* header */
.top-stripe{left:0;top:0;width:1200px;height:6px;background:var(--yellow)}
.brand{left:85px;top:24px;display:flex;align-items:center;gap:22px}
.brand-square{width:66px;height:66px;border:4px solid var(--black)}
.brand-text{font-family:"Jost",sans-serif;font-weight:500;font-size:26px;line-height:31px;color:var(--black)}
.top-social{right:97px;top:27px;display:flex;gap:14px}
.top-social span{width:17px;height:17px;border-radius:50%;background:var(--yellow);display:block}
.top-contact{right:68px;top:66px;display:flex;gap:46px;font-size:16px;color:var(--ink)}
.top-contact div{display:flex;align-items:center;gap:14px}
.top-contact svg{width:19px;height:19px}

.main-nav{left:0;top:111px;width:1200px;height:55px;background:var(--black);color:var(--white);font-size:16px}
.main-nav a{position:absolute;top:16px;color:var(--white);text-decoration:none;transform:translateX(-50%)}
.main-nav i{position:absolute;top:19px;width:1px;height:16px;background:#888}

/* hero */
.hero-photo{left:0;top:166px;width:1200px;height:588px;background:linear-gradient(180deg,#f2f1ef 0%,#e9e7e4 55%,#d9d3cb 70%,#cfc8bf 100%)}
.hero-box{left:84px;top:327px;width:513px;height:228px;background:rgba(245,245,245,.85);border:1px solid #d6d6d6;padding:38px 0 0 54px}
.hero-title{font-size:72px;font-weight:400;line-height:78px;color:#111;letter-spacing:1px}
.hero-sub{font-size:56px;font-weight:400;line-height:66px;color:#222;letter-spacing:3px}

.offer-band{left:0;top:754px;width:1200px;height:102px;background:var(--yellow)}
.offer-socks{left:67px;top:712px;width:210px;height:160px;border-radius:40px 60px 30px 50px;background:linear-gradient(135deg,#1d1d1d 0%,#3a3a3a 45%,#8a2430 60%,#a9a9a9 100%)}
.offer-text{left:322px;top:776px;display:flex;align-items:baseline;gap:16px;color:#1a1a1a}
.offer-text .lead{font-size:40px;font-weight:400}
.offer-text .rest{font-size:31px;font-weight:400}
.price-badge{left:895px;top:692px;width:184px;height:184px;border-radius:50%;background:var(--yellow-deep);border:4px solid var(--white);color:#111;text-align:center}
.price-badge .for{position:absolute;left:0;right:0;top:36px;font-size:30px;line-height:30px}
.price-badge .amount{position:absolute;left:38px;top:70px;font-size:72px;font-weight:600;line-height:72px}
.price-badge .cur{position:absolute;left:126px;top:102px;font-size:24px;transform:rotate(90deg);transform-origin:left top;left:150px;top:78px}

/* products */
.product-card{width:236px;height:384px;border:1px solid var(--card-line);background:var(--white)}
.tag-new{position:absolute;right:10px;top:10px;width:52px;height:20px;background:var(--yellow);color:var(--white);font-size:12px;text-align:center;line-height:20px}
.product-photo{position:absolute;left:40px;top:24px;width:156px;height:160px;background:linear-gradient(180deg,#f4f4f4,#dcdcdc)}
.offer-bubble{position:absolute;left:44px;top:28px;width:52px;height:42px;border-radius:50%;background:#8d8d8d;color:var(--white);font-size:8px;line-height:9px;text-align:center;padding-top:8px}
.product-title{position:absolute;left:0;right:0;top:205px;text-align:center;font-size:14px;line-height:22px;color:#333}
.product-rule{position:absolute;left:18px;right:18px;top:259px;height:1px;background:#eee}
.product-price{position:absolute;left:18px;top:268px;font-family:"Poppins",sans-serif;font-weight:600;font-size:17px;color:#111}
.product-stars{position:absolute;right:18px;top:268px;font-size:15px;letter-spacing:2px;color:var(--yellow)}
.product-stars .off{color:#ccc}
.btn-more{position:absolute;left:57px;top:322px;width:122px;height:33px;border:2px solid var(--yellow);border-radius:17px;text-align:center;line-height:29px;font-size:12px;color:#222;letter-spacing:.5px}

/* welcome */
.welcome{left:0;top:1777px;width:1200px;height:343px;background:var(--welcome-bg);text-align:center}
.welcome h2{position:absolute;left:0;right:0;top:58px;font-size:48px;font-weight:400;letter-spacing:2px;color:#222}
.welcome .rule{position:absolute;left:523px;top:134px;width:154px;height:2px;background:#aaa}
.welcome p{position:absolute;left:106px;width:988px;top:162px;font-family:"Poppins",sans-serif;font-size:17px;line-height:33px;color:#555;letter-spacing:.4px}

/* footer */
.site-footer{left:0;top:2139px;width:1200px;height:320px;background:var(--footer-bg);color:var(--footer-text)}
.foot-head{position:absolute;font-size:14px;font-weight:500;letter-spacing:.5px;color:var(--white)}
.foot-head::after{content:"";position:absolute;left:0;top:24px;width:52px;height:2px;background:var(--yellow)}
.foot-divider{position:absolute;top:90px;width:1px;height:190px;background:var(--footer-line)}
.contact-item{position:absolute;left:116px;display:flex;align-items:center;gap:20px;font-size:13px;line-height:18px}
.contact-icon{width:30px;height:30px;border-radius:50%;border:1px solid #444;display:flex;align-items:center;justify-content:center}
.contact-icon svg{width:14px;height:14px}
.foot-note{position:absolute;left:461px;top:95px;font-size:11px;line-height:20px;color:#ddd}
.foot-link{position:absolute;font-size:12px;color:#ddd}
.news-input{position:absolute;left:863px;top:105px;width:148px;height:37px;border:1px solid #888;font-size:11px;color:#999;padding:11px 12px}
.news-go{position:absolute;left:1017px;top:105px;width:54px;height:37px;background:var(--yellow);color:#1a1a1a;font-weight:600;font-size:17px;text-align:center;line-height:37px}
.foot-social{position:absolute;left:865px;top:221px;display:flex;gap:18px}
.foot-social span{width:30px;height:30px;border-radius:50%;background:var(--yellow);display:block}
.copyright{left:0;top:2459px;width:1200px;height:55px;background:var(--footer-bg);border-top:1px solid var(--footer-line);color:#ccc;font-size:12px;text-align:center;line-height:52px}
</style>
</head>
<body>

<div class="abs top-stripe"></div>

<header>
  <div class="abs brand">
    <div class="brand-square"></div>
    <div class="brand-text">Lintora – Basics i bambus -<br>lige til og enkelt</div>
  </div>
  <div class="abs top-social" aria-label="Social links"><span></span><span></span><span></span><span></span></div>
  <div class="abs top-contact">
    <div>
      <svg viewBox="0 0 20 20"><circle cx="10" cy="10" r="10" fill="#f7b92f"/><rect x="5" y="6.5" width="10" height="7" fill="none" stroke="#fff" stroke-width="1.3"/><path d="M5 6.5l5 4 5-4" fill="none" stroke="#fff" stroke-width="1.3"/></svg>
      info@lintora.dk
    </div>
    <div>
      <svg viewBox="0 0 20 20"><circle cx="10" cy="10" r="10" fill="#f7b92f"/><path d="M7 5.5l2 2-1 1.5c.8 1.5 1.6 2.3 3 3l1.5-1 2 2-1.5 1.5c-3.5-.5-6.5-3.5-7-7z" fill="#fff"/></svg>
      +45 20 14 37 52
    </div>
  </div>
</header>

<nav class="abs main-nav">
  <a style="left:141px">Forsiden</a><i style="left:216px"></i>
  <a style="left:293px">Produkter</a><i style="left:374px"></i>
  <a style="left:466px">Abonnement</a><i style="left:558px"></i>
  <a style="left:649px">Om Lintora</a><i style="left:727px"></i>
  <a style="left:804px">Hjælp</a><i style="left:871px"></i>
  <a style="left:1000px">Pengenetilbage garanti</a>
</nav>

<section>
  <div class="abs hero-photo" role="img" aria-label="Photo of a small dog sitting beside legs wearing grey knitted wool socks on a light wooden floor"></div>
  <div class="abs hero-box">
    <div class="hero-title">KEEP COOL</div>
    <div class="hero-sub">Wear Lintora</div>
  </div>
  <div class="abs offer-band"></div>
  <div class="abs offer-socks" role="img" aria-label="Packshot of a pair of black, grey and red argyle bamboo ankle socks"></div>
  <div class="abs offer-text"><span class="lead">As a test</span><span class="rest">Buy 1 pair of bamboo socks</span></div>
  <div class="abs price-badge">
    <div class="for">for only</div>
    <div class="amount">20</div>
    <div class="cur">DKK</div>
  </div>
</section>

<main>
  <!-- row 1 -->
  <div class="abs product-card" style="left:84px;top:923px">
    <div class="product-photo" role="img" aria-label="Packshot of a single black bamboo sock"></div>
    <div class="offer-bubble">Test for<br>kun kr. 20,-<br>inkl fragt</div>
    <div class="tag-new">New</div>
    <div class="product-title">Prøv vores bambusstrømper<br>kun ét par pr husstand!</div>
    <div class="product-rule"></div>
    <div class="product-price">$280.90</div>
    <div class="product-stars">★★★★<span class="off">★</span></div>
    <div class="btn-more">VIEW MORE</div>
  </div>
  <div class="abs product-card" style="left:347px;top:923px">
    <div class="product-photo" role="img" aria-label="Packshot of black and white bamboo t-shirts, tops and boxer briefs"></div>
    <div class="offer-bubble">På abon.<br>kun kr. 200,-</div>
    <div class="tag-new">New</div>
    <div class="product-title">Prøv vores bambusstrømper<br>kun ét par pr husstand!</div>
    <div class="product-rule"></div>
    <div class="product-price">$280.90</div>
    <div class="product-stars">★★★★<span class="off">★</span></div>
    <div class="btn-more">VIEW MORE</div>
  </div>
  <div class="abs product-card" style="left:612px;top:923px">
    <div class="product-photo" role="img" aria-label="Packshot of a women's set with sock, camisoles and briefs"></div>
    <div class="offer-bubble">På abon.<br>kun kr. 150,-</div>
    <div class="tag-new">New</div>
    <div class="product-title">Prøv vores bambusstrømper<br>kun ét par pr husstand!</div>
    <div class="product-rule"></div>
    <div class="product-price">$280.90</div>
    <div class="product-stars">★★★★<span class="off">★</span></div>
    <div class="btn-more">VIEW MORE</div>
  </div>
  <div class="abs product-card" style="left:875px;top:923px">
    <div class="product-photo" role="img" aria-label="Packshot of a row of black bamboo socks"></div>
    <div class="offer-bubble">På abon.<br>kun kr. 150,-</div>
    <div class="tag-new">New</div>
    <div class="product-title">Prøv vores bambusstrømper<br>kun ét par pr husstand!</div>
    <div class="product-rule"></div>
    <div class="product-price">$280.90</div>
    <div class="product-stars">★★★★<span class="off">★</span></div>
    <div class="btn-more">VIEW MORE</div>
  </div>

  <!-- row 2 -->
  <div class="abs product-card" style="left:84px;top:1339px">
    <div class="product-photo" role="img" aria-label="Photo of white bamboo briefs"></div>
    <div class="offer-bubble">På abon.<br>4 par kr. 150,-</div>
    <div class="tag-new">New</div>
    <div class="product-title">Prøv vores bambusstrømper<br>kun ét par pr husstand!</div>
    <div class="product-rule"></div>
    <div class="product-price">$280.90</div>
    <div class="product-stars">★★★★<span class="off">★</span></div>
    <div class="btn-more">VIEW MORE</div>
  </div>
  <div class="abs product-card" style="left:347px;top:1339px">
    <div class="product-photo" role="img" aria-label="Packshot of a white bamboo t-shirt"></div>
    <div class="offer-bubble">På abon.<br>kun kr. 120,-</div>
    <div class="tag-new">New</div>
    <div class="product-title">Prøv vores bambusstrømper<br>kun ét par pr husstand!</div>
    <div class="product-rule"></div>
    <div class="product-price">$280.90</div>
    <div class="product-stars">★★★★<span class="off">★</span></div>
    <div class="btn-more">VIEW MORE</div>
  </div>
  <div class="abs product-card" style="left:612px;top:1339px">
    <div class="product-photo" role="img" aria-label="Photo of a white bamboo camisole top"></div>
    <div class="offer-bubble">På abon.<br>kun kr. 102,-</div>
    <div class="tag-new">New</div>
    <div class="product-title">Prøv vores bambusstrømper<br>kun ét par pr husstand!</div>
    <div class="product-rule"></div>
    <div class="product-price">$280.90</div>
    <div class="product-stars">★★★★<span class="off">★</span></div>
    <div class="btn-more">VIEW MORE</div>
  </div>
  <div class="abs product-card" style="left:875px;top:1339px">
    <div class="product-photo" role="img" aria-label="Packshot of a black bamboo v-neck t-shirt"></div>
    <div class="offer-bubble">På abon.<br>kun kr. 120,-</div>
    <div class="tag-new">New</div>
    <div class="product-title">Prøv vores bambusstrømper<br>kun ét par pr husstand!</div>
    <div class="product-rule"></div>
    <div class="product-price">$280.90</div>
    <div class="product-stars">★★★★<span class="off">★</span></div>
    <div class="btn-more">VIEW MORE</div>
  </div>
</main>

<section class="abs welcome">
  <h2>WELCOME TO LINTORA</h2>
  <div class="rule"></div>
  <p>Bamboo clothing? Before you met us you had probably never even heard of such a thing. Bamboo is more famous for being panda food and is not (yet) associated with clothes. But this is about to change because bamboo clothing is getting more popular by the day. We will tell you here why we fell in love with bamboo, and how it is possible to make clothing from bamboo stems.</p>
</section>

<footer class="abs site-footer">
  <div class="foot-head" style="left:126px;top:57px">CONTACT INFORMATION</div>
  <div class="contact-item" style="top:120px">
    <div class="contact-icon"><svg viewBox="0 0 14 14"><path d="M7 1a4 4 0 0 1 4 4c0 3-4 8-4 8S3 8 3 5a4 4 0 0 1 4-4z" fill="#f7b92f"/><circle cx="7" cy="5" r="1.5" fill="#1c1a1b"/></svg></div>
    <div>Kornblomstvej 12, 7100 Vejle<br>Cvr 48210576</div>
  </div>
  <div class="contact-item" style="top:177px;font-weight:600">
    <div class="contact-icon"><svg viewBox="0 0 14 14"><path d="M3 1.5l2.5 2.5-1.2 1.6c.9 1.7 1.8 2.6 3.5 3.5l1.6-1.2 2.5 2.5-1.8 1.8C5.5 11.6 2.4 8.5 1.2 3.3z" fill="#f7b92f"/></svg></div>
    <div>+45 20 14 37 52</div>
  </div>
  <div class="contact-item" style="top:234px">
    <div class="contact-icon"><svg viewBox="0 0 14 14"><rect x="1.5" y="3" width="11" height="8" fill="#f7b92f"/><path d="M1.5 3l5.5 4.5L12.5 3" fill="none" stroke="#1c1a1b" stroke-width="1.2"/></svg></div>
    <div>info@lintora.dk</div>
  </div>

  <div class="foot-divider" style="left:382px"></div>

  <div class="foot-head" style="left:461px;top:57px">BE THE FIRST TO KNOW</div>
  <div class="foot-note">Soltravel.example is owned and operated by<br>Harbor Trips and offers special deals on tours to Spain</div>
  <div class="foot-head" style="left:461px;top:163px">MY ACCOUNT</div>
  <div class="foot-link" style="left:461px;top:207px">Forsiden</div>
  <div class="foot-link" style="left:461px;top:232px">Produkter</div>
  <div class="foot-link" style="left:461px;top:257px">Abonnement</div>
  <div class="foot-link" style="left:602px;top:207px">Om Lintora</div>
  <div class="foot-link" style="left:602px;top:232px">Hjælp</div>
  <div class="foot-link" style="left:602px;top:257px">Pengenetilbage garanti</div>

  <div class="foot-divider" style="left:789px"></div>

  <div class="foot-head" style="left:863px;top:57px">NEWSLETTER</div>
  <div class="news-input">Your Email Id...</div>
  <div class="news-go">GO</div>
  <div class="foot-head" style="left:863px;top:172px">SOCIAL LINKS</div>
  <div class="foot-social" aria-label="Social links"><span></span><span></span><span></span><span></span></div>
</footer>

<div class="abs copyright">Copyright © 2018 Lintora.dk.</div>

</body>
</html>
```